Owen Tasker Studios Business Card

Looking for a clear, modern, elegant, sharp business card that conveys a professional yet edgy image to my business as a wedding, portrait, and travel photographer. Would like something that looks vintage yet modern. Need a new business card to grow my business. We are growing the business for Wedding and Event Photography as well as fine art Photography. (Mostly Landscapes)
Updates

I’m looking through designs now but I have a new logo that i want using please.

New logo uploaded please redesign using that

PLEASE ALL DESIGNERS LOOK IN BRIEF FOR NEW LOGO

Target Market(s)

Brides, Grooms, Families with Kids, People looking for Fine Art Photography Artwork

Industry/Entity Type

Photographer

Contact Information for Business Card

Unsure

Font styles to use
Serif

Colors

Designer to choose colors to be used in the design.

Requirements
Must have
• My Website:
• http://taskerlens.examplefolio.net
• Phone:
• 323-481-5206
• Email:
• owentaskerlens@mailbox-example.net
Nice to have
• Would like a sort of shine on the printing finish.
• I like black I think it looks good on a business card.
• Can try working with my logo (png that I've attached)

```html
<!DOCTYPE html>
<html lang="en">
<head>
<meta charset="utf-8">
<title>Owen Tasker Studios – Business Card</title>
<link rel="stylesheet" href="https://fonts.googleapis.com/css2?family=Raleway:wght@300;400&family=Roboto:wght@400;500;700&display=swap">
<style>
  :root {
    --backdrop: #e9e7e4;
    --card-black: #1b1c1e;
    --frame-line: #a8a8a8;
    --panel-grey: #9d9d9d;
    --ink-white: #ffffff;
    --ink-soft: #f1f1f1;
  }
  * { margin: 0; padding: 0; box-sizing: border-box; }
  html, body {
    width: 1200px; height: 960px; overflow: hidden;
    background: var(--backdrop);
  }
  .canvas { position: relative; width: 1200px; height: 960px; }

  .card {
    position: absolute;
    width: 598px; height: 342px;
    background: var(--card-black);
  }
  .card--front { left: 315px; top: 113px; }
  .card--back  { left: 312px; top: 472px; }

  /* Front */
  .front-frame {
    position: absolute; left: 12px; top: 14px;
    width: 570px; height: 313px;
    border: 2px solid var(--frame-line);
    display: flex;
  }
  .brand-panel {
    width: 296px; height: 100%;
    display: flex; flex-direction: column; align-items: center; justify-content: center;
    padding-top: 8px;
  }
  .brand-square {
    width: 62px; height: 62px;
    border: 1.5px solid var(--ink-white);
    margin-bottom: 20px;
  }
  .brand-name {
    font-family: "Raleway", sans-serif;
    font-weight: 300;
    font-size: 25px;
    letter-spacing: 0.5px;
    color: var(--ink-white);
    text-transform: uppercase;
    text-align: center;
    line-height: 1.15;
  }
  .contact-panel {
    flex: 1; height: 100%;
    background: var(--panel-grey);
    display: flex; flex-direction: column; align-items: center;
    padding-top: 76px;
    font-family: "Roboto", sans-serif;
    color: var(--ink-white);
    text-align: center;
  }
  .contact-name { font-weight: 700; font-size: 20px; letter-spacing: 0.3px; }
  .contact-role { font-weight: 500; font-size: 14px; margin-top: 2px; }
  .contact-list { list-style: none; margin-top: 22px; font-size: 13.5px; line-height: 19px; }
  .contact-tagline { font-size: 14px; margin-top: 12px; }

  /* Back */
  .back-mark {
    position: absolute; left: 50%; top: 84px;
    width: 154px; height: 154px;
    margin-left: -77px;
    border: 2px solid var(--ink-white);
    display: flex; align-items: center; justify-content: center;
  }
  .back-mark-name {
    font-family: "Raleway", sans-serif;
    font-weight: 300; font-size: 17px;
    color: var(--ink-white);
    text-transform: uppercase; text-align: center;
    line-height: 1.35; letter-spacing: 1px;
  }
  .back-website {
    position: absolute; left: 0; right: 0; top: 291px;
    text-align: center;
    font-family: "Roboto", sans-serif;
    font-size: 14px; letter-spacing: 2px;
    color: var(--ink-soft);
  }
</style>
</head>
<body>
<main class="canvas">

  <section class="card card--front" aria-label="Business card front">
    <div class="front-frame">
      <div class="brand-panel">
        <div class="brand-square"></div>
        <p class="brand-name">Owen Tasker Studios</p>
      </div>
      <div class="contact-panel">
        <p class="contact-name">LEO HARTLEY</p>
        <p class="contact-role">CEO/FOUNDER</p>
        <ul class="contact-list">
          <li>P. 323-481-5206</li>
          <li>owentaskerlens@mailbox-example.net</li>
          <li>taskerlens.examplefolio.net</li>
        </ul>
        <p class="contact-tagline">Wedding &amp; Event Photography</p>
      </div>
    </div>
  </section>

  <section class="card card--back" aria-label="Business card back">
    <div class="back-mark">
      <p class="back-mark-name">Owen<br>Tasker<br>Studios</p>
    </div>
    <p class="back-website">www.taskerlens.examplefolio.net</p>
  </section>

</main>
</body>
</html>
```